Logo/Business Print Card Design

We had two businesses and had two separate logos and business cards. These two businesses have become one which is now only called Verdant Wares. We need to incorporate the characteristics and designs into 1 final logo and design under Verdant Wares.

Our Business is about sourcing products to fill in gaps in the market majority in the Retail/Grocery Market – from developing the product to designing packaging, including warehousing, and marketing the final finished product.

The logo should communicate: 1) product being sourced 2) created and developed and 3) Introduced to market and managed.

Please find attached Word Document 1 - to see the current logo and business designs that need to be incorporated.

Target Market(s)

Retailers, Buyers, Agents, Suppliers – Business to Business customers and clients we deal with.

Industry/Entity Type

Business

Requirements
Must have
• Must Have:

• The logo should communicate: 1) Sourcing 2) Developing and 3) Introducing to the Market
• The current attached illustration (image 1) shows 3 squares, the first being sourcing the product, the second indicates developing the product ready to take it to the market and the third depicts the product on the shelf ready for end consumers.
• It should be a modernized version of attached image 1.
Nice to have
• Image 2 incorporated into design
• The colour concept – company preference is Orange and Green same as Market Bridge Logo.
Should not have
• Old style fonts and designs – should be clean and uncluttered

```html
<!DOCTYPE html>
<html lang="en">
<head>
<meta charset="utf-8">
<title>Verdant Wares – Identity and Business Card</title>
<link rel="stylesheet" href="https://fonts.googleapis.com/css2?family=Source+Sans+3:wght@400;600&display=swap">
<style>
  :root {
    --orange: #ec8a2e;
    --green: #4db848;
    --lime: #b9cf2c;
    --pale: #f4f7dc;
    --blue: #45a8e0;
    --ink: #1e1e1e;
    --white: #ffffff;
  }
  * { margin: 0; padding: 0; box-sizing: border-box; }
  html, body { width: 1200px; height: 805px; overflow: hidden; background: var(--white); }
  body { position: relative; font-family: "Source Sans 3", sans-serif; }

  .brand { position: absolute; left: 6px; top: 26px; display: flex; align-items: center; gap: 10px; }
  .brand-mark { width: 22px; height: 22px; background: var(--green); }
  .brand-name { font-size: 38px; font-weight: 400; color: var(--orange); line-height: 1; }

  .card { position: absolute; top: 138px; width: 244px; height: 140px; overflow: hidden; }
  .card-front { left: 7px; background: linear-gradient(180deg, var(--lime) 0%, var(--pale) 55%, var(--white) 100%); }
  .card-back { left: 286px; background: linear-gradient(90deg, var(--lime) 0%, #8fbf8a 40%, var(--blue) 100%); color: var(--ink); }

  .card-brand { position: absolute; left: 5px; top: 16px; display: flex; align-items: center; gap: 4px; }
  .card-brand .brand-mark { width: 7px; height: 7px; }
  .card-brand .brand-name { font-size: 12px; }

  .name-line { position: absolute; font-size: 10.5px; line-height: 1; white-space: nowrap; }
  .card-front .name-line { left: 86px; top: 53px; }
  .name-line .sep { display: inline-block; width: 1px; height: 13px; vertical-align: -3px; margin: 0 6px; }
  .card-front .name { color: var(--orange); }
  .card-front .sep { background: var(--blue); }
  .card-front .title { color: var(--green); }

  .wave-art { position: absolute; left: 0; top: 68px; width: 244px; height: 72px;
    background: linear-gradient(180deg, rgba(185,207,44,0.25) 0%, #6a9a3a 40%, #9cc6d8 65%, rgba(255,255,255,0.6) 100%); }

  .card-back .name-line { left: 2px; top: 4px; color: var(--white); }
  .card-back .sep { background: var(--white); }
  .qualifications { position: absolute; left: 2px; top: 17px; color: var(--white); font-size: 7px; font-weight: 600; line-height: 9.4px; }

  .contact { position: absolute; font-size: 6.6px; line-height: 9.2px; }
  .contact dt { float: left; clear: left; width: 10px; font-weight: 600; }
  .contact dd { margin-left: 10px; }
  .contact-main { left: 46px; top: 51px; }
  .contact-extra { left: 130px; top: 51px; }
  .contact-post { left: 69px; top: 95px; }
</style>
</head>
<body>
  <header class="brand">
    <span class="brand-mark"></span>
    <span class="brand-name">Verdant Wares</span>
  </header>

  <section class="card card-front">
    <div class="card-brand">
      <span class="brand-mark"></span>
      <span class="brand-name">Verdant Wares</span>
    </div>
    <p class="name-line"><span class="name">Name</span><span class="sep"></span><span class="title">Title</span></p>
    <div class="wave-art" role="img" aria-label="Flowing green and blue wave illustration with soft lime circles"></div>
  </section>

  <section class="card card-back">
    <p class="name-line"><span class="name">Name</span><span class="sep"></span><span class="title">Title</span></p>
    <p class="qualifications">Cualifications<br>Cualifications<br>Cualifications</p>
    <dl class="contact contact-main">
      <dt>t.</dt><dd>+55 [5]5 5555 5555</dd>
      <dt>m.</dt><dd>+55 [5]555 555 555</dd>
      <dt>e.</dt><dd>email@domain.com</dd>
      <dt>w.</dt><dd>www.domain.com</dd>
    </dl>
    <dl class="contact contact-extra">
      <dt>f.</dt><dd>+55 [5]5 5555 5555</dd>
      <dt>s.</dt><dd>[skype] skypeid</dd>
    </dl>
    <dl class="contact contact-post">
      <dt>p.</dt><dd>PO BOX 555, city, state 5555 australia</dd>
      <dt>a.</dt><dd>suite 5, 555 streetname<br>city, state 555</dd>
    </dl>
  </section>
</body>
</html>
```